Eco-friendly waste company needs flyer design to promote collections

We need a flyer to promote our new small item collection service, offering cheaper waste collections to customers who usually would not want to pay for our high-eco performance business (we are expensive compared to companies who dispose of their waste in less eco-friendly ways). This flyer needs to be professional, informational, and classy to appeal to corporate office-based customers. We want photos used where possible, not cartoon or illustrations of objects we collect. I will attach our logo in various designs, and am really open to design options. We have a website that is ourdated, uses cartoons etc, and this is not landing well with our customer base so we want to move away from that kind of design. I need an A5-sized flyer, double sided. Please ask me if you have any questions!
Hi all,
Thank you all so much for so many wonderful designs, I will be looking through all of these tomorrow with my CEO and then I will update the project status again.
Thanks!!
Kind regards,
Mira

Hi all,
Thanks!!
Kind regards,
Mira

```html
<!DOCTYPE html>
<html lang="en">
<head>
<meta charset="utf-8">
<title>Greenloop Collect – Small Item Collections Flyer</title>
<link href="https://fonts.googleapis.com/css2?family=Montserrat:wght@400;500;600;700;800&display=swap" rel="stylesheet">
<style>
  :root{
    --green:#2a9d78;
    --green-light:#36b08a;
    --green-dark:#14704f;
    --ink:#2e2f2a;
    --charcoal:#3a3a34;
    --band:#ebebeb;
    --paper:#ffffff;
    --bg:#efefef;
  }
  *{box-sizing:border-box;margin:0;padding:0}
  html,body{width:783px;height:1200px;overflow:hidden;background:var(--bg)}
  body{font-family:"Montserrat",Arial,sans-serif;color:var(--ink)}
  .flyer{position:absolute;left:11px;top:62px;width:760px;height:1075px;background:var(--paper);overflow:hidden;box-shadow:0 2px 10px rgba(0,0,0,.12)}
  .abs{position:absolute}
  .header-art{position:absolute;left:0;top:0}
  /* brand */
  .brand{left:52px;top:68px;display:flex;align-items:center;gap:12px}
  .brand-mark{width:16px;height:16px;background:var(--green)}
  .brand-name{font-size:24px;font-weight:700;line-height:28px;letter-spacing:.3px;color:var(--charcoal)}
  .brand-tagline{left:52px;top:106px;font-size:10.5px;font-weight:600;color:var(--green);letter-spacing:.3px}
  /* headline */
  .headline{left:51px;top:190px;color:#fff;font-weight:700;text-transform:uppercase}
  .headline span{display:block}
  .headline .kicker{font-size:21px;line-height:25px;font-weight:600;letter-spacing:.3px}
  .headline .big{font-size:42px;line-height:48px;font-weight:700;letter-spacing:-1px}
  .headline .huge{font-size:53px;line-height:58px;font-weight:700;letter-spacing:-1.5px}
  .rule{left:51px;top:356px;width:300px;height:1px;background:rgba(255,255,255,.55)}
  .rule::before{content:"";position:absolute;left:0;top:-1.5px;width:68px;height:4px;border-radius:2px;background:#fff}
  .intro{left:53px;top:372px;width:205px;font-size:11.5px;line-height:14.5px;color:#fff}
  .intro b{font-weight:700}
  .divider{left:263px;top:370px;height:48px;border-left:1px dashed rgba(255,255,255,.7)}
  .price{left:275px;top:362px;color:#fff}
  .price .amount{font-size:40px;font-weight:700;line-height:40px}
  .price .each{font-size:16px;font-weight:400}
  .price .day{font-size:14px;font-weight:700;display:block}
  /* items */
  .items-band{left:0;top:494px;width:760px;height:222px;background:var(--band)}
  .items-tab{left:57px;top:472px}
  .items-title{left:70px;top:476px;font-size:19px;font-weight:600;color:#fff;letter-spacing:.4px}
  .items{list-style:none;font-size:12px;font-weight:600;color:var(--ink)}
  .items li{position:relative;height:30.5px;padding-left:28px;line-height:16px}
  .tick{position:absolute;left:0;top:1px;width:13px;height:13px}
  .items-left{left:57px;top:530px}
  .items-right{left:322px;top:530px}
  /* photos */
  .photo{top:738px;width:193px;height:127px;border:3px solid #fff;box-shadow:0 1px 5px rgba(0,0,0,.3)}
  .photo-1{left:61px;background:linear-gradient(135deg,#4d6a3a,#8b7b6a 45%,#c7523a 70%,#5a6fb0)}
  .photo-2{left:280px;background:linear-gradient(160deg,#e7ecf1,#c9d4de 50%,#2fa257 75%,#3d4350)}
  .photo-3{left:508px;background:linear-gradient(180deg,#3f78c9,#8fb3e0 45%,#e9ecef 65%,#8b8f93)}
  /* conditions */
  .cond-title{left:57px;top:889px;font-size:17.5px;font-weight:600;color:var(--ink);letter-spacing:.3px}
  .cond-title span{color:var(--green)}
  .conditions{list-style:none;left:57px;top:921px;font-size:13.5px;font-weight:500;color:var(--ink)}
  .conditions li{position:relative;padding-left:28px;line-height:17px;margin-bottom:17px}
  .conditions .tick{top:2px}
  /* challenge */
  .challenge{left:405px;top:891px}
  .challenge-note{left:420px;top:906px;width:140px;font-size:10.5px;line-height:12.5px;color:#fff}
  .challenge-cta{left:595px;top:918px;font-size:11px;font-weight:700;color:#fff;letter-spacing:.3px}
  /* footer */
  .email{left:57px;top:1033px;font-size:12px;font-weight:700;color:var(--ink);display:flex;align-items:center;gap:10px}
  .call{left:419px;top:1008px;color:#fff;font-weight:700;white-space:nowrap}
  .call .label{font-size:17px;letter-spacing:.6px}
  .call .number{font-size:20.5px;letter-spacing:1px;margin-left:6px}
  .web{left:419px;top:1034px;color:#fff;font-size:13.5px;font-weight:700;display:flex;align-items:center;gap:7px}
</style>
</head>
<body>
<main class="flyer">

  <svg class="header-art" width="760" height="470" viewBox="0 0 760 470">
    <defs>
      <linearGradient id="photoTone" x1="0" y1="0" x2="1" y2="1">
        <stop offset="0" stop-color="#f3efe6"/>
        <stop offset="0.45" stop-color="#a9a49a"/>
        <stop offset="0.7" stop-color="#d8d23a"/>
        <stop offset="1" stop-color="#2f3550"/>
      </linearGradient>
      <linearGradient id="panelGreen" x1="0" y1="0" x2="0" y2="1">
        <stop offset="0" stop-color="#33ad87"/>
        <stop offset="1" stop-color="#14704f"/>
      </linearGradient>
    </defs>
    <rect x="300" y="0" width="460" height="434" fill="url(#photoTone)" role="img" aria-label="Photo of a smiling warehouse worker in a high-visibility vest working on a laptop"/>
    <polygon points="0,0 370,0 318,160 0,160" fill="#fff"/>
    <path d="M480,434 C520,470 560,462 570,434 Z" fill="#1f4a36"/>
    <path d="M0,154 L364,154 C408,154 418,190 424,236 C436,336 466,432 566,458 L0,458 Z" fill="#fff"/>
    <path d="M0,156 L360,156 C400,156 410,192 416,236 C428,336 458,430 552,456 L0,456 Z" fill="url(#panelGreen)"/>
  </svg>

  <div class="abs brand"><span class="brand-mark"></span><span class="brand-name">GREENLOOP COLLECT</span></div>
  <div class="abs brand-tagline">CLEANER COLLECTIONS FOR LONDON</div>

  <h1 class="abs headline">
    <span class="kicker">Do you have small or</span>
    <span class="big">Single items</span>
    <span class="huge">That cost</span>
    <span class="kicker">Too much to dispose of?</span>
  </h1>
  <div class="abs rule"></div>
  <p class="abs intro">Are you located in <b>Central London?</b> Greenloop has the solution for you. We can collect</p>
  <div class="abs divider"></div>
  <p class="abs price"><span class="amount">£25</span><span class="each"> EACH</span><span class="day">on Wednesdays</span></p>

  <div class="abs items-band"></div>
  <svg class="abs items-tab" width="290" height="36" viewBox="0 0 290 36">
    <path d="M255,36 C262,6 272,0 290,4 L290,36 Z" fill="#595955"/>
    <path d="M0,0 L250,0 C262,0 268,6 272,12 C262,18 256,28 252,36 L0,36 Z" fill="#3a3a34"/>
  </svg>
  <h2 class="abs items-title">EXAMPLE ITEMS ARE</h2>

  <ul class="abs items items-left">
    <li><svg class="tick" viewBox="0 0 14 14"><circle cx="7" cy="7" r="7" fill="#2a9d78"/><path d="M4 7.2l2 2 4-4.2" stroke="#fff" stroke-width="1.6" fill="none"/></svg>Printers</li>
    <li><svg class="tick" viewBox="0 0 14 14"><circle cx="7" cy="7" r="7" fill="#2a9d78"/><path d="M4 7.2l2 2 4-4.2" stroke="#fff" stroke-width="1.6" fill="none"/></svg>Office furniture</li>
    <li><svg class="tick" viewBox="0 0 14 14"><circle cx="7" cy="7" r="7" fill="#2a9d78"/><path d="M4 7.2l2 2 4-4.2" stroke="#fff" stroke-width="1.6" fill="none"/></svg>Whiteboards</li>
    <li><svg class="tick" viewBox="0 0 14 14"><circle cx="7" cy="7" r="7" fill="#2a9d78"/><path d="M4 7.2l2 2 4-4.2" stroke="#fff" stroke-width="1.6" fill="none"/></svg>Shredders</li>
    <li><svg class="tick" viewBox="0 0 14 14"><circle cx="7" cy="7" r="7" fill="#2a9d78"/><path d="M4 7.2l2 2 4-4.2" stroke="#fff" stroke-width="1.6" fill="none"/></svg>PC or television monitors</li>
    <li><svg class="tick" viewBox="0 0 14 14"><circle cx="7" cy="7" r="7" fill="#2a9d78"/><path d="M4 7.2l2 2 4-4.2" stroke="#fff" stroke-width="1.6" fill="none"/></svg>Fans</li>
  </ul>
  <ul class="abs items items-right">
    <li><svg class="tick" viewBox="0 0 14 14"><circle cx="7" cy="7" r="7" fill="#2a9d78"/><path d="M4 7.2l2 2 4-4.2" stroke="#fff" stroke-width="1.6" fill="none"/></svg>Plants and planter boxes</li>
    <li><svg class="tick" viewBox="0 0 14 14"><circle cx="7" cy="7" r="7" fill="#2a9d78"/><path d="M4 7.2l2 2 4-4.2" stroke="#fff" stroke-width="1.6" fill="none"/></svg>Books and magazines (max 25kg)</li>
    <li><svg class="tick" viewBox="0 0 14 14"><circle cx="7" cy="7" r="7" fill="#2a9d78"/><path d="M4 7.2l2 2 4-4.2" stroke="#fff" stroke-width="1.6" fill="none"/></svg>Pallet</li>
    <li><svg class="tick" viewBox="0 0 14 14"><circle cx="7" cy="7" r="7" fill="#2a9d78"/><path d="M4 7.2l2 2 4-4.2" stroke="#fff" stroke-width="1.6" fill="none"/></svg>Packaging (cardboard boxes, polystyrene, plastic etc.)</li>
    <li><svg class="tick" viewBox="0 0 14 14"><circle cx="7" cy="7" r="7" fill="#2a9d78"/><path d="M4 7.2l2 2 4-4.2" stroke="#fff" stroke-width="1.6" fill="none"/></svg>Paints and chemicals (max 7 litres)</li>
    <li><svg class="tick" viewBox="0 0 14 14"><circle cx="7" cy="7" r="7" fill="#2a9d78"/><path d="M4 7.2l2 2 4-4.2" stroke="#fff" stroke-width="1.6" fill="none"/></svg>Light bulbs and fluorescent tubes (max 10 pieces)</li>
  </ul>

  <div class="abs photo photo-1" role="img" aria-label="Photo of a pile of dumped bags and household waste beside a litter bin"></div>
  <div class="abs photo photo-2" role="img" aria-label="Photo of two crew members in green shirts clearing an office"></div>
  <div class="abs photo photo-3" role="img" aria-label="Photo of a white collection truck with crew loading items"></div>

  <h2 class="abs cond-title">CONDITIONS <span>OF OFFER</span></h2>
  <ul class="abs conditions">
    <li><svg class="tick" viewBox="0 0 14 14"><circle cx="7" cy="7" r="7" fill="#2a9d78"/><path d="M4 7.2l2 2 4-4.2" stroke="#fff" stroke-width="1.6" fill="none"/></svg>Price is exclusive of VAT.</li>
    <li><svg class="tick" viewBox="0 0 14 14"><circle cx="7" cy="7" r="7" fill="#2a9d78"/><path d="M4 7.2l2 2 4-4.2" stroke="#fff" stroke-width="1.6" fill="none"/></svg>Eligible postcodes: EC1, EC2, EC3, EC4,<br>WC1, WC2, W1, SW1, SE1, E1, E2, N1, NW1</li>
  </ul>

  <svg class="abs challenge" width="296" height="70" viewBox="0 0 296 70">
    <rect x="0" y="0" width="296" height="70" rx="14" fill="#36b08a"/>
    <path d="M14,0 L183,0 C168,8 162,30 158,48 C154,62 146,70 130,70 L14,70 A14,14 0 0 1 0,56 L0,14 A14,14 0 0 1 14,0 Z" fill="#3a3a34"/>
  </svg>
  <p class="abs challenge-note">We can take most things you can't put in your normal bins</p>
  <p class="abs challenge-cta">CHALLENGE US!</p>

  <svg class="abs" style="left:0;top:975px" width="760" height="100" viewBox="0 0 760 100">
    <defs>
      <linearGradient id="footGreen" x1="0" y1="0" x2="0" y2="1">
        <stop offset="0" stop-color="#33ad87"/>
        <stop offset="1" stop-color="#14704f"/>
      </linearGradient>
    </defs>
    <path d="M360,100 C366,40 384,8 430,6 L760,6 L760,100 Z" fill="#3a3a34"/>
    <path d="M370,100 C376,42 394,10 440,8 L760,8 L760,100 Z" fill="#fff"/>
    <path d="M376,100 C382,46 400,14 446,12 L760,0 L760,100 Z" fill="url(#footGreen)"/>
    <rect x="0" y="96" width="18" height="4" fill="#3a3a34"/>
    <rect x="18" y="96" width="360" height="4" fill="#2a9d78"/>
  </svg>

  <p class="abs email">
    <svg width="17" height="12" viewBox="0 0 17 12"><rect x="0.5" y="0.5" width="16" height="11" fill="#2a9d78"/><path d="M0.5 0.5l8 6 8-6M0.5 11.5l6-5M16.5 11.5l-6-5" stroke="#fff" stroke-width="1" fill="none"/></svg>
    hello@greenloopcollect.com
  </p>
  <p class="abs call"><span class="label">CALL US NOW:</span><span class="number">020 7946 0321</span></p>
  <p class="abs web">
    <svg width="13" height="13" viewBox="0 0 13 13"><circle cx="6.5" cy="6.5" r="5.8" stroke="#fff" stroke-width="1.1" fill="none"/><ellipse cx="6.5" cy="6.5" rx="2.6" ry="5.8" stroke="#fff" stroke-width="1" fill="none"/><path d="M0.8 6.5h11.4M1.8 3.6h9.4M1.8 9.4h9.4" stroke="#fff" stroke-width="0.9"/></svg>
    www.greenloopcollect.com
  </p>

</main>
</body>
</html>
```